Contemporary Media Company with Logo Needs Business Card Design

Need a modern card design for a full service digital media company using the logo included. Also want the info below on the card. Probably list the services on the card back to save space for the front. Want something contemporary to impress prospective clients. You may want to submit both a somewhat more conservative design, and then a more wild one.
General Info: (this phrase need not be on the card)
Tod Parvin
Founder and CEO
949-628-4513
tod@lumavantstudio.example
lumavantstudio.example
Services: (this word need not be on the card)
Content & Experience Strategy
Brand Development
Search Engine Optimization
Website Design
Website Operation
Social Media Integration
Complete Video Solutions
Industry/Entity Type
Business
Contact Information for Business Card
Tod Parvin
Founder and CEO
949-628-4513
tod@lumavantstudio.example
lumavantstudio.example
Brand Development
Website Design
Website Operation
Social Media Integration
Complete Video Solutions
Look and feel

```html
<!DOCTYPE html>
<html lang="en">
<head>
<meta charset="utf-8">
<title>Lumavant Studio – Business Card</title>
<link rel="stylesheet" href="https://fonts.googleapis.com/css2?family=Arimo:wght@400;700&family=Montserrat:wght@500&family=Tinos&display=swap">
<style>
  :root {
    --backdrop: #ecebe8;
    --card: #ffffff;
    --ink: #1a1a1a;
    --accent: #f0961e;
    --muted: #5a5a5a;
    --globe: #7a6a55;
    --shadow: rgba(0, 0, 0, 0.12);
  }
  * { box-sizing: border-box; margin: 0; padding: 0; }
  html, body { width: 1200px; height: 1000px; overflow: hidden; }
  body {
    background: var(--backdrop);
    display: flex;
    align-items: center;
    justify-content: center;
    gap: 40px;
  }
  .card {
    position: relative;
    width: 520px;
    height: 297px;
    background: var(--card);
    box-shadow: 0 6px 18px var(--shadow);
  }
  .card-front {
    display: flex;
    align-items: center;
    justify-content: center;
  }
  .wordmark {
    display: flex;
    align-items: center;
    gap: 14px;
    font-family: "Montserrat", sans-serif;
    font-weight: 500;
    letter-spacing: 0.12em;
    text-transform: uppercase;
  }
  .wordmark-square { display: block; background: currentColor; }
  .card-front .wordmark { color: var(--ink); font-size: 30px; }
  .card-front .wordmark-square { width: 30px; height: 30px; }
  .card-back .wordmark {
    position: absolute;
    left: 38px;
    top: 190px;
    color: var(--muted);
    font-size: 17px;
  }
  .card-back .wordmark-square { width: 16px; height: 16px; }
  .contact {
    position: absolute;
    left: 300px;
    top: 34px;
    list-style: none;
  }
  .contact-name {
    font-family: "Arimo", sans-serif;
    font-weight: 700;
    font-size: 20px;
    color: var(--accent);
  }
  .contact-role {
    font-family: "Arimo", sans-serif;
    font-size: 12px;
    color: var(--muted);
    margin-bottom: 14px;
  }
  .contact-line {
    display: flex;
    flex-direction: column;
    gap: 4px;
    margin-bottom: 12px;
    font-family: "Tinos", serif;
    font-size: 14px;
    color: var(--ink);
  }
  .contact-line svg { width: 22px; height: 22px; }
</style>
</head>
<body>
  <section class="card card-front" aria-label="Card front">
    <div class="wordmark"><span class="wordmark-square"></span>Lumavant Studio</div>
  </section>

  <section class="card card-back" aria-label="Card back">
    <div class="wordmark"><span class="wordmark-square"></span>Lumavant Studio</div>
    <ul class="contact">
      <li class="contact-name">Tod Parvin</li>
      <li class="contact-role">Founder (CEO)</li>
      <li class="contact-line">
        <svg viewBox="0 0 22 22" aria-hidden="true">
          <circle cx="11" cy="11" r="11" fill="var(--accent)"/>
          <rect x="7.5" y="4.5" width="7" height="13" rx="1.5" fill="none" stroke="#fff" stroke-width="1.4"/>
          <line x1="9.5" y1="15.3" x2="12.5" y2="15.3" stroke="#fff" stroke-width="1.2"/>
        </svg>
        <span>949-628-4513</span>
      </li>
      <li class="contact-line">
        <svg viewBox="0 0 22 22" aria-hidden="true">
          <rect x="1" y="4" width="20" height="14" fill="var(--accent)"/>
          <polyline points="1,4 11,12 21,4" fill="none" stroke="#fff" stroke-width="1.3"/>
        </svg>
        <span>tod@lumavantstudio.example</span>
      </li>
      <li class="contact-line">
        <svg viewBox="0 0 22 22" aria-hidden="true">
          <circle cx="11" cy="11" r="10" fill="var(--globe)"/>
          <g fill="none" stroke="#fff" stroke-width="1">
            <ellipse cx="11" cy="11" rx="4.5" ry="9"/>
            <line x1="1" y1="11" x2="21" y2="11"/>
            <line x1="11" y1="1" x2="11" y2="21"/>
            <path d="M3 6.5 H19 M3 15.5 H19"/>
          </g>
        </svg>
        <span>lumavantstudio.example</span>
      </li>
    </ul>
  </section>
</body>
</html>
```